Wine Bottle Label Graphic Design (mini bottle 187ml)

Looking for a contemporary custom wine label design for party favors. Inspiration photos provided. **Please see "wine favorite" example in uploads.

Artwork 2.5" wide by 2.75" tall to be placed on 3"x3" stickers. Specs from printer attached but I still want image to fit within the artwork size I specified. Please make label center justified. This is for BOYS. It does not need to be super "masculine"...but definitely not feminine.

Required elements:

Colors: white background, include gold and purple to match logo. Other colors are fine to include.

Name: Sababa 13 (I like use of the No) as shown in the sample, but not required
Varietal: Mitzvah Blend 6.11.2021
Vineyard: Hollis Family Vineyard
Location: Maryland
Logo: See attached (KRNotecard Final)

Font styles to use
Serif
Sans Serif

Requirements
Must have
• All the above elements. Clean and crisp design. Contemporary and classy. Purple, Gold, Black colors. See logo. You CAN include cursive font for select elements. I don't mind a combination of print and script.
Should not have
• Floral, scrolling, background image, old fashioned

```html
<!DOCTYPE html>
<html lang="en">
<head>
<meta charset="UTF-8">
<title>Sababa 13 — Mitzvah Blend Label</title>
<link rel="stylesheet" href="https://fonts.googleapis.com/css2?family=Playfair+Display:wght@400;700;900&family=Yellowtail&display=swap">
<style>
  :root {
    --backdrop: #6f6865;
    --backdrop-light: #8d8784;
    --label-white: #ffffff;
    --purple: #4a2b86;
    --purple-deep: #3b2170;
    --gold-light: #f6dd8a;
    --gold: #dcae3c;
    --gold-deep: #b8862a;
    --ink-grey: #4b4750;
  }
  * { margin: 0; padding: 0; box-sizing: border-box; }
  html, body { width: 1200px; height: 654px; overflow: hidden; }
  body {
    background: radial-gradient(ellipse at 50% 45%, var(--backdrop-light), var(--backdrop));
    position: relative;
  }
  .label {
    position: absolute;
    left: 328px;
    top: 27px;
    width: 544px;
    height: 600px;
    background: var(--label-white);
    border-radius: 8px;
    overflow: hidden;
    box-shadow: 0 6px 18px rgba(0,0,0,0.25);
  }
  .top-band {
    position: absolute; left: 0; top: 0; width: 100%; height: 126px;
    background: linear-gradient(180deg, var(--purple-deep), var(--purple));
  }
  .gold-rule {
    position: absolute; left: 0; top: 126px; width: 100%; height: 11px;
    background: linear-gradient(90deg, var(--gold-deep), var(--gold-light) 30%, var(--gold) 60%, var(--gold-light) 85%, var(--gold-deep));
  }
  .brand-seal {
    position: absolute; left: 176px; top: 30px; width: 192px; height: 192px;
    border-radius: 50%;
    background: var(--purple);
    display: flex; align-items: center; justify-content: center;
  }
  .brand-name {
    font-family: "Playfair Display", serif;
    font-weight: 700;
    font-size: 22px;
    letter-spacing: 2px;
    color: var(--label-white);
    text-align: center;
    line-height: 1.2;
  }
  .wine-name {
    position: absolute; left: 0; top: 250px; width: 100%;
    text-align: center;
    font-family: "Playfair Display", serif;
    font-weight: 900;
    font-size: 56px;
    letter-spacing: 3px;
    color: var(--purple);
  }
  .details {
    position: absolute; right: 56px; top: 386px;
    text-align: right;
  }
  .varietal {
    font-family: "Playfair Display", serif;
    font-weight: 700;
    font-size: 20px;
    letter-spacing: 6px;
    color: var(--purple);
  }
  .vintage {
    font-family: "Playfair Display", serif;
    font-weight: 400;
    font-size: 15px;
    letter-spacing: 4px;
    color: var(--ink-grey);
    margin-top: 4px;
  }
  .vineyard {
    font-family: "Yellowtail", cursive;
    font-size: 27px;
    color: var(--purple);
    margin-top: 6px;
  }
  .region {
    font-family: "Playfair Display", serif;
    font-size: 13px;
    letter-spacing: 4px;
    color: var(--ink-grey);
    margin-top: 6px;
  }
  .bottom-rule {
    position: absolute; left: 0; top: 525px; width: 100%; height: 13px;
    background: var(--purple);
  }
  .gold-band {
    position: absolute; left: 0; top: 538px; width: 100%; height: 62px;
    background: linear-gradient(90deg, var(--gold-deep), var(--gold) 20%, var(--gold-light) 45%, var(--gold) 70%, var(--gold-deep));
  }
</style>
</head>
<body>
  <main class="label">
    <div class="top-band"></div>
    <div class="gold-rule"></div>
    <div class="brand-seal">
      <div class="brand-name">KAI &amp;<br>REUBEN</div>
    </div>
    <h1 class="wine-name">SABABA 13</h1>
    <section class="details">
      <div class="varietal">MITZVAH BLEND</div>
      <div class="vintage">2021</div>
      <div class="vineyard">Hollis Family Vineyard</div>
      <div class="region">MARYLAND</div>
    </section>
    <div class="bottom-rule"></div>
    <div class="gold-band" role="img" aria-label="Gold foil band with fine wavy line pattern"></div>
  </main>
</body>
</html>
```